HARD MONEY ORIGINATOR RECRUITMENT.
Looking for individuals to help us originate loans for real estate investor financing primarily used to fix up properties and resell.
HARD MONEY ORIGINATORS WANTED
No Licensing Required
Work As Independent Contractor
1% Flat Finders Fee on Each Loan
Referral Compensation for Recruiting New Originators
Immediate Payouts
Programs Offered Nationwide
Marketing Assistance and Support Available
Email mpelton@brightquaylending.com for more information or call (800) 641-2950 Ext. 24 Brightquay Lending Services, Inc. www.brightquaylending.com NMLS #318760
Industry/Entity Type
Real Estate
Look and feel
Each slider illustrates characteristics of the customer's brand and the style your logo design should communicate.

```html
<!DOCTYPE html>
<html lang="en">
<head>
<meta charset="utf-8">
<title>Hard Money Originator Recruitment</title>
<link href="https://fonts.googleapis.com/css2?family=Open+Sans:wght@400;600;700&family=Montserrat:wght@600&display=swap" rel="stylesheet">
<style>
:root{
  --page-bg:#e9ecef;
  --white:#ffffff;
  --brand-blue:#0b5e8a;
  --heading-blue:#1f6394;
  --box-line:#1d5f8f;
  --box-text:#4a4a4a;
  --gold:#bea83f;
  --hero-light:#d9e2ea;
  --hero-mid:#7f9fbb;
  --hero-deep:#2f6a98;
}
*{box-sizing:border-box;margin:0;padding:0}
html,body{width:929px;height:1200px;overflow:hidden;background:var(--page-bg)}
body{font-family:"Open Sans",Arial,sans-serif;position:relative}
.flyer{position:absolute;left:39px;top:0;width:850px;height:1200px;background:var(--white);overflow:hidden}
.brand{position:absolute;left:68px;top:66px;display:flex;align-items:center;gap:10px}
.brand-dot{width:30px;height:30px;border-radius:50%;background:var(--gold)}
.brand-name{font-family:"Open Sans",Arial,sans-serif;font-weight:700;font-size:17px;color:var(--brand-blue);line-height:1.15}
.call{position:absolute;right:87px;top:64px;font-family:"Montserrat",Arial,sans-serif;font-weight:600;font-size:27px;color:var(--brand-blue);letter-spacing:.3px}
.hero{position:absolute;left:0;top:159px;width:850px;height:511px}
.hero-photo{position:absolute;inset:0;background:linear-gradient(90deg,var(--hero-light) 0%,#b9c9d8 35%,var(--hero-mid) 58%,var(--hero-deep) 100%)}
.hero-copy{position:absolute;left:530px;top:112px;width:200px;text-align:center;color:var(--white)}
.hero-title{font-weight:700;font-size:33px;line-height:39px;letter-spacing:.3px;margin-left:-40px;margin-right:-40px}
.hero-text{margin-top:24px;font-weight:600;font-size:17.5px;line-height:22.3px}
.wanted{position:absolute;left:0;top:714px;width:850px;text-align:center;font-weight:700;font-size:26px;color:var(--heading-blue);letter-spacing:.2px}
.perk{position:absolute;border:2px solid var(--box-line);border-radius:13px;display:flex;align-items:center;justify-content:center;text-align:center;font-size:16.5px;line-height:20px;color:var(--box-text);padding:0 8px}
.footer{position:absolute;left:0;top:1011px;width:850px;height:189px;background:var(--brand-blue)}
.more{position:absolute;left:0;top:56px;width:307px;height:77px;background:var(--gold);border-radius:0 38px 38px 0;display:flex;align-items:center;padding-left:47px;color:var(--white);font-weight:700;font-size:22px}
.contact{position:absolute;left:336px;top:55px;color:var(--white);font-size:16.6px;line-height:20.5px}
.contact .email{margin-left:14px}
.nmls{position:absolute;left:340px;top:127px;color:var(--white);font-size:16.6px}
</style>
</head>
<body>
<main class="flyer">
  <header>
    <div class="brand"><span class="brand-dot"></span><span class="brand-name">Brightquay<br>Lending</span></div>
    <div class="call">CALL (800) 641-2950</div>
  </header>

  <section class="hero">
    <div class="hero-photo" role="img" aria-label="Photo of a row of smiling business professionals in suits, fading into a blue office backdrop"></div>
    <div class="hero-copy">
      <h1 class="hero-title">HARD MONEY ORIGINATOR RECRUITMENT</h1>
      <p class="hero-text">Looking for individuals to help us originate loans for real estate investor financing primarily used to fix up properties and resell.</p>
    </div>
  </section>

  <h2 class="wanted">HARD MONEY ORIGINATORS WANTED</h2>

  <div class="perk" style="left:59px;top:795px;width:138px;height:79px">No Licensing Required</div>
  <div class="perk" style="left:211px;top:795px;width:179px;height:79px">1% Flat Finders Fee on Each Loan</div>
  <div class="perk" style="left:402px;top:795px;width:246px;height:79px">Referral Compensation for Recruiting New Originators</div>
  <div class="perk" style="left:661px;top:795px;width:131px;height:79px">Immediate Payouts</div>
  <div class="perk" style="left:59px;top:889px;width:243px;height:79px">Work As Independent Contractor</div>
  <div class="perk" style="left:317px;top:889px;width:249px;height:79px">Marketing Assistance and Support Available</div>
  <div class="perk" style="left:579px;top:889px;width:213px;height:79px">Programs Offered Nationwide</div>

  <footer class="footer">
    <div class="more">For more information</div>
    <p class="contact">Brightquay Lending Services, Inc.<br>407 West Harbor Avenue, Suite<br>210, Annapolis, MD 21401<span class="email">mpelton@brightquaylending.com</span></p>
    <p class="nmls">NMLS #318760</p>
  </footer>
</main>
</body>
</html>
```